IT Consultancy Web Site

We need a twitter bootstrap, hero based designed for our IT Consultancy firm based in Adelaide, Australia called "Velmora IT Consulting". We provide custom software development. We have some core areas of the site we wish to develop further at a later point. A blog, an ecommerce shop, and products / services listings - All three of these should have clearly visible navigation below the hero.

The final design should be clean and minimalist. It should communicate professionalism and elegance.

Industry/Entity Type

Shop

Requirements
Nice to have
• We currently do not have a logo, so inclusion of something simple in the design would be a bonus

```html
<!DOCTYPE html>
<html lang="en">
<head>
<meta charset="utf-8">
<title>Velmora IT Consulting</title>
<link href="https://fonts.googleapis.com/css2?family=Roboto:ital,wght@0,300;0,400;0,500;0,700;1,700&family=Roboto+Slab:wght@400;700&display=swap" rel="stylesheet">
<style>
:root{
  --teal:#1a9e84;
  --teal-dark:#158a72;
  --red:#ee3e57;
  --red-dark:#d8324a;
  --blue:#1f6fc4;
  --navy:#1d3f6e;
  --ink:#333b44;
  --muted:#7a828a;
  --light:#ececec;
  --white:#ffffff;
}
*{box-sizing:border-box;margin:0;padding:0}
html,body{width:1200px;height:4248px;overflow:hidden}
body{font-family:'Roboto',Arial,sans-serif;color:var(--ink);background:var(--white);position:relative}
.abs{position:absolute}
.btn{position:absolute;display:flex;align-items:center;justify-content:center;gap:14px;color:var(--white);font-weight:500;font-size:20px;border-radius:3px;white-space:nowrap}
.btn-teal{background:var(--teal);box-shadow:0 4px 0 var(--teal-dark)}
.btn-red{background:var(--red)}

/* header */
.site-header{top:0;left:0;width:1200px;height:131px;background:var(--white)}
.brand{left:140px;top:36px;display:flex;align-items:center;gap:14px}
.brand-dot{width:56px;height:56px;border-radius:50%;background:var(--navy)}
.brand-name{font-size:24px;font-weight:500;color:var(--navy);line-height:1.1;width:200px}
.main-nav{right:100px;top:0;display:flex;height:131px}
.nav-item{width:100px;display:flex;flex-direction:column;align-items:center;justify-content:center;gap:10px;font-size:14px;color:var(--teal)}
.nav-item.active{background:var(--white);box-shadow:0 0 14px rgba(0,0,0,.15);color:var(--ink)}
.nav-icon{width:24px;height:20px;border:3px solid var(--teal);border-radius:4px}
.nav-item.active .nav-icon{border-color:var(--ink);border-radius:50%}

/* hero */
.hero{top:131px;left:0;width:1200px;height:595px;background:linear-gradient(160deg,#2e7bd0 0%,#1c5aa6 50%,#173f7a 100%)}
.hero h1{position:absolute;top:40px;width:100%;text-align:center;color:var(--white);font-size:40px;font-weight:700}
.hero .lead{position:absolute;top:100px;width:100%;text-align:center;color:#e6efff;font-size:22px;font-family:'Roboto Slab',serif}
.hero .btn-red{left:440px;top:145px;width:320px;height:62px;font-size:22px}
.slider-dots{left:140px;top:528px;display:flex;gap:10px}
.slider-dots span{width:8px;height:8px;border-radius:50%;background:rgba(255,255,255,.5)}
.slider-dots span:first-child{background:var(--white)}
.hero-actions{left:400px;top:508px;display:flex;background:#14345f;border-radius:24px;height:50px;width:330px}
.hero-actions div{flex:1;display:flex;align-items:center;justify-content:center;gap:10px;color:var(--white);font-size:17px;font-weight:500}
.play{width:26px;height:18px;background:var(--white);border-radius:9px}
.hero-social{right:100px;top:520px;display:flex;gap:8px}
.hero-social span{width:20px;height:20px;border-radius:50%;background:rgba(255,255,255,.55)}

/* feature */
.feature{top:726px;left:0;width:1200px;height:779px}
.feature-photo{width:100%;height:100%;background:linear-gradient(100deg,#e9ecef 0%,#c9d2da 40%,#8b96a2 70%,#cdd4dc 100%)}
.card{position:absolute;padding:40px 36px}
.feature-card{left:637px;top:36px;width:425px;height:600px;background:var(--white);box-shadow:0 6px 20px rgba(0,0,0,.2)}
.card-tag{display:flex;align-items:center;gap:10px;font-size:18px;font-weight:500;color:var(--teal)}
.tag-icon{width:20px;height:16px;border:3px solid currentColor;border-radius:3px}
.feature-card h2{margin-top:28px;font-size:44px;line-height:1.12;font-weight:300;color:var(--teal)}
.accent{display:block;margin-top:22px;font-size:40px;font-style:italic;font-weight:700;color:var(--red)}
.card p.small{margin-top:28px;font-size:15px;line-height:1.7;color:var(--muted)}
.feature-card .btn{left:36px;top:480px;width:220px;height:62px}

/* core areas */
.core{top:1505px;left:0;width:1200px;height:382px;background:var(--teal)}
.core h2{position:absolute;top:45px;width:100%;text-align:center;color:#d6f1ea;font-size:31px;font-weight:300}
.core h2 b{color:var(--white);font-weight:400}
.core-list{position:absolute;top:130px;left:120px;width:960px;display:flex}
.core-item{flex:1;text-align:center;color:var(--white);border-right:1px solid rgba(255,255,255,.2)}
.core-item:last-child{border:none}
.core-circle{width:135px;height:135px;margin:0 auto;border-radius:50%;background:rgba(255,255,255,.14);display:flex;align-items:center;justify-content:center}
.core-item.active .core-circle{background:var(--white)}
.core-item h3{margin-top:16px;font-size:17px;font-weight:500}
.core-item p{font-size:13px;color:#c9ece3;margin-top:4px}

/* about */
.about{top:1887px;left:0;width:1200px;height:616px}
.about-photo{width:100%;height:100%;background:linear-gradient(100deg,#f3d9a6 0%,#f1e3c3 45%,#d9c7ab 65%,#f6ecd9 100%)}
.about-card{left:141px;top:42px;width:425px;height:506px;background:var(--red);color:var(--white)}
.about-card .card-tag{color:var(--white)}
.about-card h2{margin-top:26px;font-size:36px;line-height:1.2;font-weight:300}
.about-card .accent{color:var(--white);font-size:36px;margin-top:0;display:inline}
.about-card p.small{color:#ffe3e7}
.about-card .btn{left:36px;top:400px;width:262px;height:62px}

/* products */
.products{top:2503px;left:0;width:1200px;height:577px;background:var(--white)}
.section-title{position:absolute;width:100%;text-align:center;font-family:'Roboto Slab',serif;font-size:30px;color:var(--red)}
.products .section-title{top:32px}
.product{position:absolute;top:108px;width:284px;height:361px;padding:24px 22px;color:var(--white)}
.product h3{font-size:31px;font-weight:700;font-style:italic;line-height:1.05}
.product p{font-size:12px;line-height:1.5;margin-top:10px;opacity:.85}
.product-shot{position:absolute;left:22px;right:22px;bottom:30px;height:160px;border-radius:4px}
.p1{left:141px;background:var(--blue)}
.p2{left:460px;background:#2f3a48}
.p3{left:779px;background:var(--teal)}
.products .btn-all{left:355px;top:500px;width:240px;height:56px}
.products .btn-shop{left:615px;top:500px;width:230px;height:56px}

/* blog */
.blog{top:3080px;left:0;width:1200px;height:665px;background:linear-gradient(180deg,#f0455e,#e63a53)}
.blog-title{position:absolute;top:40px;left:141px;display:flex;gap:12px;align-items:center;color:var(--white);font-size:26px;font-family:'Roboto Slab',serif}
.blog-post{position:absolute;top:118px;width:284px;height:420px;background:var(--white)}
.blog-photo{height:200px;background:linear-gradient(135deg,#f2c79a,#d98b5e)}
.blog-body{padding:18px 18px}
.blog-body h3{color:var(--red);font-size:18px;font-weight:700}
.blog-body p{margin-top:8px;font-size:14px;line-height:1.55;color:var(--muted)}
.blog-meta{position:absolute;left:18px;right:18px;bottom:16px;display:flex;justify-content:space-between;font-size:12px;color:#9aa0a6;border-top:1px solid #eee;padding-top:10px}
.b1{left:141px}.b2{left:460px}.b3{left:779px}
.blog .btn{left:490px;top:576px;width:220px;height:58px}

/* connect */
.connect{top:3745px;left:0;width:1200px;height:432px;background:var(--light)}
.connect h2{position:absolute;top:40px;width:100%;text-align:center;font-family:'Roboto Slab',serif;font-size:30px;font-weight:400;color:var(--ink)}
.connect .intro{position:absolute;top:94px;width:100%;text-align:center;font-size:15px;line-height:1.6;color:var(--muted)}
.field{position:absolute;left:141px;width:337px;height:34px;background:var(--white);border:1px solid #ddd;font-size:13px;color:#999;padding:8px 12px}
.field-name{top:172px}
.field-email{top:216px}
.connect .btn-red{left:141px;top:262px;width:337px;height:38px;font-size:14px}
.tweet{position:absolute;left:640px;top:168px;width:430px}
.tweet-head{display:flex;align-items:center;gap:12px;color:var(--teal);font-size:22px;font-family:'Roboto Slab',serif}
.tweet-dot{width:40px;height:40px;border-radius:50%;background:var(--teal)}
.tweet p{margin-top:12px;font-size:16px;line-height:1.55;font-style:italic;color:var(--muted);font-family:'Roboto Slab',serif}
.tweet small{display:block;margin-top:6px;font-size:12px;color:#aaa}
.social-row{position:absolute;top:360px;width:100%;display:flex;justify-content:center;gap:14px}
.social-row span{width:40px;height:40px;border-radius:50%;background:#b8bcc0}

/* footer */
.site-footer{top:4177px;left:0;width:1200px;height:71px;background:var(--white);display:flex;align-items:center;justify-content:space-between;padding:0 141px;font-size:14px;color:var(--muted)}
</style>
</head>
<body>

<header class="site-header abs">
  <div class="brand abs"><span class="brand-dot"></span><span class="brand-name">Velmora IT Consulting</span></div>
  <nav class="main-nav abs">
    <div class="nav-item"><span class="nav-icon"></span>About Us</div>
    <div class="nav-item active"><span class="nav-icon"></span>Services</div>
    <div class="nav-item"><span class="nav-icon"></span>Products</div>
    <div class="nav-item"><span class="nav-icon"></span>Shop</div>
    <div class="nav-item"><span class="nav-icon"></span>Blogs</div>
    <div class="nav-item"><span class="nav-icon"></span>Contact Us</div>
  </nav>
</header>

<section class="hero abs" role="img" aria-label="Team of developers working together at computers, tinted blue">
  <h1>Get your Consulting of amazing software development</h1>
  <p class="lead">Use Velmora IT Consulting to collect research, stories, inspiration and notes</p>
  <div class="btn btn-red">See Plans and Pricing</div>
  <div class="slider-dots abs"><span></span><span></span><span></span><span></span></div>
  <div class="hero-actions abs"><div><span class="play"></span>Watch Video</div><div>Get started</div></div>
  <div class="hero-social abs"><span></span><span></span><span></span></div>
</section>

<section class="feature abs">
  <div class="feature-photo" role="img" aria-label="Young developer with glasses working at a computer in an office"></div>
  <div class="card feature-card">
    <div class="card-tag"><span class="tag-icon"></span>Software Development</div>
    <h2>See the companies, startups and entrepreneurs</h2>
    <span class="accent">you will find here.</span>
    <p class="small">Here, innovative people have the chance to put their ideas into practice, share experiences, get away from isolation and work surrounded by cool people.</p>
    <div class="btn btn-teal">Meet Velmora IT <span>›</span></div>
  </div>
</section>

<section class="core abs">
  <h2>We have some core areas of the <b>Velmora IT Consulting</b> services.</h2>
  <div class="core-list">
    <div class="core-item">
      <div class="core-circle"><svg width="56" height="50" viewBox="0 0 56 50"><rect x="2" y="2" width="40" height="30" rx="2" fill="#fff"/><rect x="16" y="34" width="12" height="8" fill="#fff"/><rect x="8" y="42" width="28" height="5" fill="#fff"/><rect x="44" y="10" width="10" height="37" rx="2" fill="#fff"/></svg></div>
      <h3>New Technology</h3><p>Get best new ways</p>
    </div>
    <div class="core-item active">
      <div class="core-circle"><svg width="50" height="50" viewBox="0 0 50 50"><rect x="4" y="4" width="42" height="42" rx="4" fill="none" stroke="#1a9e84" stroke-width="5"/><rect x="17" y="15" width="16" height="20" fill="#1a9e84"/></svg></div>
      <h3>Advanced Protection</h3><p>You are safe here</p>
    </div>
    <div class="core-item">
      <div class="core-circle"><svg width="52" height="52" viewBox="0 0 52 52"><rect x="4" y="8" width="40" height="36" rx="6" fill="#fff"/><circle cx="38" cy="38" r="11" fill="#1a9e84" stroke="#fff" stroke-width="4"/></svg></div>
      <h3>Software Architect</h3><p>Creation of software</p>
    </div>
    <div class="core-item">
      <div class="core-circle"><svg width="56" height="50" viewBox="0 0 56 50"><rect x="2" y="2" width="44" height="32" rx="2" fill="#fff"/><circle cx="44" cy="36" r="8" fill="#fff"/><rect x="34" y="42" width="20" height="6" rx="3" fill="#fff"/></svg></div>
      <h3>Systems Analyst</h3><p>Get issues solved</p>
    </div>
  </div>
</section>

<section class="about abs">
  <div class="about-photo" role="img" aria-label="Businesswoman holding binders in a warm lit office"></div>
  <div class="card about-card">
    <div class="card-tag"><span class="tag-icon"></span>About Velmora IT Consulting</div>
    <h2>With Notebin you can articles, watch videos, share notes &amp; more. <span class="accent">you will find here.</span></h2>
    <p class="small">Here, innovative people have the chance to put their ideas into practice, share experiences, get away from isolation and work surrounded by cool people.</p>
    <div class="btn btn-teal">Get More Information <span>›</span></div>
  </div>
</section>

<section class="products abs">
  <h2 class="section-title">View Our Product</h2>
  <article class="product p1">
    <h3>Development product - 1</h3>
    <p>Lorem ipsum is simply dummy text of printing and typesetting industry.</p>
    <div class="product-shot" role="img" aria-label="Product screens on laptop and tablet" style="background:#e8eef6"></div>
  </article>
  <article class="product p2">
    <h3>Development product - 2</h3>
    <p>Lorem ipsum is simply dummy text of printing and typesetting.</p>
    <div class="product-shot" role="img" aria-label="Desktop monitor showing product dashboard" style="background:#56647a"></div>
  </article>
  <article class="product p3">
    <h3>Development product - 3</h3>
    <p>Lorem ipsum is simply dummy text of printing.</p>
    <div class="product-shot" role="img" aria-label="Round preview of product interface" style="background:#e9f5f2;border-radius:50%;left:52px;right:52px;height:180px"></div>
  </article>
  <div class="btn btn-teal btn-all">View All Products</div>
  <div class="btn btn-red btn-shop">Visit Our Shop <span>›</span></div>
</section>

<section class="blog abs">
  <div class="blog-title"><svg width="24" height="24" viewBox="0 0 24 24"><rect x="2" y="2" width="20" height="20" fill="none" stroke="#fff" stroke-width="3"/><path d="M7 12l4 4 7-8" fill="none" stroke="#fff" stroke-width="3"/></svg>Latest in Blog</div>
  <article class="blog-post b1">
    <div class="blog-photo" role="img" aria-label="Woman working on a laptop"></div>
    <div class="blog-body"><h3>Lorem Ipsum is simply</h3><p>Lorem Ipsum is simply dummy text of printing and typesetting industry. lorem ipsum.</p></div>
    <div class="blog-meta"><span>24.08.2013</span><span>Comments</span></div>
  </article>
  <article class="blog-post b2">
    <div class="blog-photo" role="img" aria-label="Woman working on a laptop"></div>
    <div class="blog-body"><h3>Lorem Ipsum is simply</h3><p>Lorem Ipsum is simply dummy text of printing and typesetting industry. lorem ipsum.</p></div>
    <div class="blog-meta"><span>24.08.2013</span><span>Comments</span></div>
  </article>
  <article class="blog-post b3">
    <div class="blog-photo" role="img" aria-label="Woman working on a laptop"></div>
    <div class="blog-body"><h3>Lorem Ipsum is simply</h3><p>Lorem Ipsum is simply dummy text of printing and typesetting industry. Share experiences...</p></div>
    <div class="blog-meta"><span>24.08.2013</span><span>Comments</span></div>
  </article>
  <div class="btn btn-teal">View All Blogs</div>
</section>

<section class="connect abs">
  <h2>Stay Connected</h2>
  <p class="intro">Whether it's joining us on the social side or signing up to our Newsletter,<br>stay in the loop with the latest news, features and goodies from Velmora IT</p>
  <div class="field field-name">Name</div>
  <div class="field field-email">Your email</div>
  <div class="btn btn-red">Subscribe Now!</div>
  <div class="tweet">
    <div class="tweet-head"><span class="tweet-dot"></span>@velmora_notes</div>
    <p>Lorem Ipsum is simply dummy text of printing and typesetting industry. Lorem Ipsum has been industry's standard dummy text ever.</p>
    <small>34 hours ago</small>
  </div>
  <div class="social-row"><span></span><span></span><span></span><span></span><span></span></div>
</section>

<footer class="site-footer abs">
  <span>Copyright © 2013 Velmora IT Consulting. All Rights Reserved.</span>
  <span>Home / About Us / Services / Products / Shop / Blogs / Contact Us</span>
</footer>

</body>
</html>
```